Lawn sign for construction company

Would like this to be a very clean and high end design for luxury homes. We need a yard sign designed that includes the company logo, website, phone number and major service offerings (residential and commercial renovations and maintenance)
The company website is brambleworks.com all other contact info is in the attachments
Target Market(s)
Luxury home owners and business owners
Industry/Entity Type
Construction/Home Improvement
Font styles to use
Other font styles liked:
- See company logo and other graphics included for title text fonts. All other fonts can be standard sans serif.
Colors
0054AA
0677BA
7BADD7
CADEEF
E8F1F8
Requirements
Must have
- Clean, easy to read design, would like 2 sided sign. A main sign side and back side which states “free estimates, and includes the website and phone number. Must also match the color scheme of the provided logo and other company images. Dark Navy blue primary color, gray secondary color, and orange as an accent color.
Nice to have
- 2nd sign side very simple design
Should not have
- Too many graphics limit to 1-3 colors

```html
<!DOCTYPE html>
<html lang="en">
<head>
<meta charset="utf-8">
<title>Bramble Works Company – Lawn Sign, Front and Back</title>
<link rel="stylesheet" href="https://fonts.googleapis.com/css2?family=Open+Sans:wght@400&family=Oswald:wght@600&family=Questrial&family=Saira+Stencil+One&display=swap">
<style>
  :root {
    --board-light: #e6e7e8;
    --board-dark: #d1d2d4;
    --paper: #ffffff;
    --accent-orange: #e37828;
    --mark-gray: #6a6a6b;
    --ink: #111111;
  }
  * { margin: 0; padding: 0; box-sizing: border-box; }
  html, body { width: 1200px; height: 491px; overflow: hidden; }
  body { position: relative; background: var(--board-light); }
  .board-diagonal { position: absolute; inset: 0; width: 1200px; height: 491px; }
  .side-label {
    position: absolute; top: 28px; width: 493px; text-align: center;
    font-family: "Open Sans", sans-serif; font-size: 56px; line-height: 1;
    color: var(--ink);
  }
  .side-label--front { left: 86px; }
  .side-label--back { left: 620px; }
  .sign {
    position: absolute; top: 112px; width: 493px; height: 323px;
    background: var(--paper); box-shadow: 0 1px 3px rgba(0,0,0,.25);
  }
  .sign--front { left: 86px; }
  .sign--back { left: 620px; }
  .sign__frame {
    position: absolute; left: 17px; right: 17px; top: 17px; height: 253px;
    border: 7px solid var(--accent-orange); border-bottom: none;
  }
  .sign__brand {
    position: absolute; left: 0; right: 0; display: flex; flex-direction: column;
    align-items: center; gap: 8px;
  }
  .sign--front .sign__brand { top: 50px; }
  .sign--back .sign__brand { top: 40px; }
  .brand-mark { width: 92px; height: 92px; border-radius: 50%; background: var(--mark-gray); }
  .brand-name {
    font-family: "Oswald", sans-serif; font-weight: 600; font-size: 24px;
    line-height: 1; color: var(--accent-orange); text-transform: uppercase;
  }
  .offer {
    position: absolute; left: 0; right: 0; top: 222px; text-align: center;
    font-family: "Oswald", sans-serif; font-weight: 600; font-size: 33px;
    line-height: 1; color: var(--accent-orange);
  }
  .services {
    position: absolute; left: 0; right: 0; top: 196px; text-align: center;
    list-style: none; font-family: "Saira Stencil One", sans-serif;
    font-size: 17px; line-height: 21px; letter-spacing: 5px;
    color: var(--accent-orange);
  }
  .sign__footer {
    position: absolute; left: 0; right: 0; bottom: 0; height: 54px;
    background: var(--accent-orange); display: flex; align-items: center;
    justify-content: center; gap: 14px;
    font-family: "Questrial", sans-serif; font-size: 24px; color: var(--paper);
  }
  .sign__divider { width: 3px; height: 18px; background: var(--paper); }
</style>
</head>
<body>
  <svg class="board-diagonal" viewBox="0 0 1200 491" aria-hidden="true">
    <polygon points="0,491 1200,0 1200,491" fill="var(--board-dark)"/>
  </svg>

  <h2 class="side-label side-label--front">Front</h2>
  <h2 class="side-label side-label--back">Back</h2>

  <section class="sign sign--front">
    <div class="sign__frame"></div>
    <div class="sign__brand">
      <span class="brand-mark" aria-hidden="true"></span>
      <span class="brand-name">Bramble Works Company</span>
    </div>
    <p class="offer">FREE ESTIMATES</p>
    <footer class="sign__footer">
      <span>brambleworks.com</span><span class="sign__divider"></span><span>555 201 480 0</span>
    </footer>
  </section>

  <section class="sign sign--back">
    <div class="sign__frame"></div>
    <div class="sign__brand">
      <span class="brand-mark" aria-hidden="true"></span>
      <span class="brand-name">Bramble Works Company</span>
    </div>
    <ul class="services">
      <li>GENERAL CONTRACTING</li>
      <li>PROPERTY MANAGEMENT</li>
      <li>REMODELING</li>
    </ul>
    <footer class="sign__footer">
      <span>brambleworks.com</span><span class="sign__divider"></span><span>555 201 480 0</span>
    </footer>
  </section>
</body>
</html>
```